Brochure required

Looking at getting business brochure designed for my solar sales company. i will require a range of products to be listed on the brochure I require a simple/ elegent / professional looking brochure.

I am happy to provide designer with all the required information that must go into the brochure. otherwise please visit www.velorquintade.com.au and view the products which i would like to allocate into the brochure aswell as our company logo and a little about me section

```html
<!DOCTYPE html>
<html lang="en">
<head>
<meta charset="utf-8">
<title>Velorquintade – Energy Solutions Brochure</title>
<link rel="stylesheet" href="https://fonts.googleapis.com/css2?family=Roboto:wght@300;400;500;700;900&display=swap">
<style>
  :root {
    --blue: #1283b8;
    --yellow: #e2c32f;
    --teal: #17b28c;
    --ink: #1b2230;
    --grey: #5f6064;
    --body: #808285;
    --canvas: #f3f4f6;
    --white: #ffffff;
    --photo-sky: linear-gradient(160deg, #a9c3d8 0%, #5f7894 45%, #1f3158 100%);
    --photo-panel: linear-gradient(170deg, #3b5a8a 0%, #1a2c57 55%, #0e1a38 100%);
  }
  * { margin: 0; padding: 0; box-sizing: border-box; }
  html, body { width: 1200px; height: 836px; overflow: hidden; background: var(--canvas); }
  body { font-family: "Roboto", sans-serif; }
  .stage { position: relative; width: 1286px; height: 896px; transform: scale(0.93313); transform-origin: 0 0; }
  .page { position: absolute; top: 18px; width: 612px; height: 860px; background: var(--white); overflow: hidden; }
  .page--cover { left: 25px; }
  .page--services { left: 657px; }
  .shapes { position: absolute; inset: 0; width: 612px; height: 860px; }
  .photo { position: absolute; }

  /* cover */
  .cover-title { position: absolute; left: 40px; top: 74px; }
  .cover-title__main { display: block; font-size: 98px; font-weight: 900; color: var(--blue); line-height: 1; letter-spacing: 1px; }
  .cover-title__sub { display: block; font-size: 68px; font-weight: 400; color: var(--grey); line-height: 1; margin-top: 4px; letter-spacing: 1px; }
  .cover-title__tag { display: block; font-size: 28px; font-weight: 300; color: var(--grey); margin-top: 6px; letter-spacing: .5px; }
  .contact { position: absolute; left: 0; right: 0; top: 742px; text-align: center; }
  .contact__title { font-size: 20px; font-weight: 400; color: var(--blue); letter-spacing: .5px; }
  .contact__line { margin-top: 6px; font-size: 14px; color: var(--grey); display: flex; justify-content: center; align-items: center; gap: 8px; }
  .contact__icon { width: 17px; height: 17px; }

  /* services */
  .brand { position: absolute; left: 258px; top: 30px; display: flex; align-items: center; gap: 10px; }
  .brand__mark { width: 26px; height: 26px; background: var(--teal); }
  .brand__name { font-size: 40px; font-weight: 700; color: var(--ink); letter-spacing: -.5px; }
  .banner-title { position: absolute; left: 25px; top: 137px; font-size: 38px; font-weight: 700; color: var(--white); display: flex; gap: 12px; }
  .banner-title__box { background: var(--ink); color: var(--yellow); padding: 0 8px; }
  .banner-tag { position: absolute; left: 33px; top: 193px; font-size: 20px; font-weight: 500; color: var(--ink); }
  .intro { position: absolute; left: 25px; top: 550px; }
  .intro__title { font-size: 30px; font-weight: 700; color: var(--blue); line-height: 1; }
  .intro__sub { font-size: 15px; color: var(--blue); margin-top: 5px; }
  .services { position: absolute; left: 25px; top: 614px; width: 568px; display: grid; grid-template-columns: 278px 262px; grid-template-rows: 87px auto; column-gap: 28px; }
  .service__title { font-size: 16px; font-weight: 500; color: var(--blue); line-height: 1.2; white-space: nowrap; letter-spacing: -.1px; }
  .service__text { font-size: 11px; font-weight: 300; color: var(--body); line-height: 1.27; text-align: justify; margin-top: 1px; }
  .footer-url { position: absolute; right: 28px; top: 816px; font-size: 15px; color: var(--white); }
</style>
</head>
<body>
<div class="stage">

  <section class="page page--cover">
    <svg class="shapes" viewBox="0 0 612 860">
      <polygon points="380,0 612,0 612,117 445,117" fill="var(--blue)"/>
      <polygon points="0,313 380,313 430,178 612,178 612,660 420,660 385,717 0,717" fill="var(--yellow)"/>
      <polygon points="0,804 95,804 70,860 0,860" fill="var(--blue)"/>
      <polygon points="105,804 612,804 612,860 78,860" fill="var(--yellow)"/>
    </svg>
    <div class="photo" role="img" aria-label="Installer in hard hat carrying a solar panel across a rooftop array"
         style="inset:0;background:var(--photo-sky);clip-path:polygon(10px 323px,368px 323px,248px 532px,352px 660px,440px 660px,400px 703px,10px 703px);"></div>
    <div class="photo" role="img" aria-label="Two workers fitting a solar panel on a tiled house roof"
         style="inset:0;background:linear-gradient(170deg,#b9cfe4 0%,#6d7f93 50%,#7a4a36 100%);clip-path:polygon(460px 203px,604px 203px,604px 417px,352px 417px);"></div>
    <div class="photo" role="img" aria-label="Pole-mounted solar panel against a blue sky"
         style="inset:0;background:linear-gradient(160deg,#2f4f7a 0%,#6f9fd0 60%,#9cc4ea 100%);clip-path:polygon(300px 433px,604px 433px,604px 633px,360px 633px,262px 532px);"></div>

    <h1 class="cover-title">
      <span class="cover-title__main">ENERGY</span>
      <span class="cover-title__sub">SOLUTIONS</span>
      <span class="cover-title__tag">For A CHANGING WORLD</span>
    </h1>

    <div class="contact">
      <p class="contact__title">CONTACT US</p>
      <p class="contact__line">
        <svg class="contact__icon" viewBox="0 0 20 20" aria-hidden="true"><circle cx="10" cy="10" r="10" fill="var(--blue)"/><circle cx="10" cy="10" r="6" fill="none" stroke="#fff" stroke-width="1.3"/><path d="M4 10h12M10 4c-3 3-3 9 0 12M10 4c3 3 3 9 0 12" fill="none" stroke="#fff" stroke-width="1.1"/></svg>
        <span>www.velorquintade.com.au</span>
        <span>|</span>
        <svg class="contact__icon" viewBox="0 0 20 20" aria-hidden="true"><circle cx="10" cy="10" r="10" fill="var(--blue)"/><path d="M7 5l2 3-1.2 1.2c.6 1.4 1.6 2.4 3 3L12 11l3 2-1 2c-4 0-8-4-8-8z" fill="#fff"/></svg>
        <span>0400 555 019</span>
      </p>
    </div>
  </section>

  <section class="page page--services">
    <div class="photo" role="img" aria-label="Close view of rows of blue solar panels"
         style="left:0;top:180px;width:612px;height:354px;background:var(--photo-panel);"></div>
    <svg class="shapes" viewBox="0 0 612 860">
      <polygon points="0,0 95,0 150,102 0,102" fill="var(--blue)"/>
      <polygon points="108,0 132,0 190,102 166,102" fill="var(--yellow)"/>
      <polygon points="255,257 612,257 612,280 255,280" fill="var(--teal)"/>
      <polygon points="0,102 448,102 488,180 448,257 0,257" fill="var(--yellow)"/>
      <polygon points="363,552 418,552 448,585 393,585" fill="var(--yellow)"/>
      <polygon points="433,552 612,552 612,585 458,585" fill="var(--blue)"/>
      <polygon points="0,804 93,804 66,860 0,860" fill="var(--blue)"/>
      <polygon points="103,804 612,804 612,860 78,860" fill="var(--yellow)"/>
    </svg>

    <div class="brand">
      <span class="brand__mark"></span>
      <span class="brand__name">Velorquintade</span>
    </div>

    <h2 class="banner-title"><span class="banner-title__box">ENERGY</span><span>SOLUTIONS</span></h2>
    <p class="banner-tag">FOR A CHANGING WORLD.</p>

    <div class="intro">
      <h3 class="intro__title">WE PRIDE OURSELVES</h3>
      <p class="intro__sub">On providing premium quality solar services</p>
    </div>

    <div class="services">
      <article class="service">
        <h4 class="service__title">SYSTEM MAINTENANC &amp; CLEANING</h4>
        <p class="service__text">Just like running a car, regular servicing is the best way to ensure your solar panel system keeps operating safely, correctly and efficiently.</p>
      </article>
      <article class="service">
        <h4 class="service__title">MAINTENANCE SCHEDULES</h4>
        <p class="service__text">It is important that regular maintenance is carried out on your solar panel system. Undertaking regular maintenance will ensure your solar panel system is operating safely, correctly and efficiently.</p>
      </article>
      <article class="service">
        <h4 class="service__title">SOLAR INSTALLATION AUDITING</h4>
        <p class="service__text">Installers are required to provide systems that meet Australian standards and only around 8% were able to meet them with only minor deviations. Just 2.5% were rated as “industry best practice”, that is the installation exceeded Australian standards.</p>
      </article>
      <article class="service">
        <h4 class="service__title">SOLAR SYSTEM MONITORING</h4>
        <p class="service__text">Solar power is a fantastic long-term investment that can help you substantially cut your greenhouse emissions and electricity bills. In order to ensure you get the greatest efficiency out of your system we strongly recommend that you monitor it regularly.</p>
      </article>
    </div>

    <p class="footer-url">www.velorquintade.com.au</p>
  </section>

</div>
</body>
</html>
```